Boutique personal training and fitness studio - banner ad design

We need a 'revolving' banner ad designed for our personal training and fitness studio. There are three separate offers (i.e. 3 pages to the advertisements)
Offer 1
PT Starter Pack
3 personal training sessions
$119
New clients only
Offer 2
Group fitness
2 weeks unlimited group fitness classes
$29
New clients only
Offer 3
Strength starter pack
2 weeks unlimited group fitness classes and 2 PT sessions
$89
New clients only
Please do not put the words "Offer 1, 2 or 3" in the ads - just the text following each offer.
Each advertisement should be sized to fit across around half of the webpage and be in landscape format.
Each advertisement should have a suitable picture (no cartoons) and should be complimentary to the existing website.
Each advertisement should also include the logo (attached)
www.corrabankliftworks.com.au
Training

```html
<!DOCTYPE html>
<html lang="en">
<head>
<meta charset="utf-8">
<title>PT Starter Pack – Banner Ads</title>
<link rel="stylesheet" href="https://fonts.googleapis.com/css2?family=Oswald:wght@500;700&family=Tinos&display=swap">
<style>
  :root {
    --board: #a56a3d;
    --panel: #1b1b1b;
    --panel-line: #232323;
    --cream: #f3ead2;
    --white: #ffffff;
    --blue: #1a9bd8;
    --blue-dark: #0d6fae;
    --red: #b8171c;
    --red-dark: #7a0b0f;
    --silver-hi: #ffffff;
    --silver-lo: #8d8d8d;
  }
  * { box-sizing: border-box; margin: 0; padding: 0; }
  html, body { width: 1200px; height: 967px; overflow: hidden; }
  body { background: var(--board); position: relative; font-family: "Oswald", sans-serif; }

  .board-heading {
    position: absolute; left: 227px; top: 24px;
    font-family: "Oswald", sans-serif; font-weight: 500; font-size: 44px;
    color: var(--white); letter-spacing: 0.5px;
  }

  .banner {
    position: absolute; left: 227px; width: 780px; height: 388px;
    background: repeating-linear-gradient(45deg, var(--panel) 0 3px, var(--panel-line) 3px 5px);
    overflow: hidden;
  }
  .banner--gym { top: 100px; }
  .banner--strength { top: 512px; }

  .banner__art { position: absolute; inset: 0; width: 780px; height: 388px; }

  .banner__copy {
    position: absolute; right: 19px; top: 66px; text-align: right;
  }
  .banner__title {
    font-family: "Oswald", sans-serif; font-weight: 700; font-size: 58px; line-height: 60px;
    text-transform: uppercase;
    background: linear-gradient(180deg, var(--silver-hi) 0%, #d9d9d9 45%, var(--silver-lo) 55%, #e6e6e6 100%);
    -webkit-background-clip: text; background-clip: text; color: transparent;
  }
  .banner__subtitle {
    margin-top: 10px;
    font-family: "Oswald", sans-serif; font-weight: 700; font-size: 27px; line-height: 30px;
    color: var(--cream); text-transform: uppercase;
  }

  .banner__ribbon {
    position: absolute; left: 480px; top: 282px; width: 300px; height: 49px;
    display: flex; align-items: center; justify-content: flex-end; padding-right: 10px;
    font-family: "Tinos", serif; font-size: 24px; color: var(--white); text-transform: uppercase;
    clip-path: polygon(0 0, 100% 0, 100% 100%, 0 100%, 16px 50%);
  }
  .banner--gym .banner__ribbon { background: var(--blue); }
  .banner--strength .banner__ribbon { background: var(--red); }

  .banner__price {
    position: absolute; left: 331px; top: 245px; width: 108px; height: 108px; border-radius: 50%;
    border: 3px solid var(--white);
    display: flex; align-items: center; justify-content: center;
    font-family: "Oswald", sans-serif; font-weight: 500; font-size: 36px; color: var(--white);
    box-shadow: 0 2px 6px rgba(0,0,0,0.5);
  }
  .banner--gym .banner__price { background: radial-gradient(circle at 40% 30%, #5cc4f2, var(--blue) 55%, var(--blue-dark)); }
  .banner--strength .banner__price { background: radial-gradient(circle at 40% 30%, #e0454a, var(--red) 55%, var(--red-dark)); }

  .banner__brand {
    position: absolute; left: 20px; bottom: 22px;
    font-family: "Oswald", sans-serif; font-weight: 500; font-size: 15px; line-height: 1;
    color: var(--white); letter-spacing: 1px; text-transform: uppercase;
  }
</style>
</head>
<body>
  <h1 class="board-heading">OFFER 1</h1>

  <section class="banner banner--gym">
    <svg class="banner__art" viewBox="0 0 780 388" aria-hidden="false">
      <defs>
        <linearGradient id="gymPhoto" x1="0" y1="0" x2="1" y2="1">
          <stop offset="0" stop-color="#c9d3da"/>
          <stop offset="0.45" stop-color="#8a8f95"/>
          <stop offset="1" stop-color="#3a3d42"/>
        </linearGradient>
      </defs>
      <polygon role="img" aria-label="Photo: man pressing dumbbells on a gym bench" points="0,0 498,0 348,388 0,388" fill="url(#gymPhoto)"/>
      <line x1="503" y1="0" x2="353" y2="388" stroke="#ffffff" stroke-width="4"/>
    </svg>
    <div class="banner__copy">
      <h2 class="banner__title">PT Starter<br>Pack</h2>
      <p class="banner__subtitle">3 Personal Training<br>Sessions</p>
    </div>
    <div class="banner__ribbon">New clients only!</div>
    <div class="banner__price">$119</div>
    <p class="banner__brand">Corrabank Liftworks</p>
  </section>

  <section class="banner banner--strength">
    <svg class="banner__art" viewBox="0 0 780 388">
      <defs>
        <linearGradient id="strengthPhoto" x1="0" y1="0" x2="1" y2="1">
          <stop offset="0" stop-color="#4a3a33"/>
          <stop offset="0.5" stop-color="#b89a82"/>
          <stop offset="1" stop-color="#e6d7c4"/>
        </linearGradient>
      </defs>
      <polygon role="img" aria-label="Photo: athlete lifting dumbbells to her shoulders" points="0,0 498,0 348,388 0,388" fill="url(#strengthPhoto)"/>
      <line x1="503" y1="0" x2="353" y2="388" stroke="#ffffff" stroke-width="4"/>
    </svg>
    <div class="banner__copy">
      <h2 class="banner__title">PT Starter<br>Pack</h2>
      <p class="banner__subtitle">3 Personal Training<br>Sessions</p>
    </div>
    <div class="banner__ribbon">New clients only!</div>
    <div class="banner__price">$119</div>
    <p class="banner__brand">Corrabank Liftworks</p>
  </section>
</body>
</html>
```